Website design for legal tech start up in Switzerland (B2B)

We are for a legal tech start up in Switzerland called TAVO. We have been running since August 2016. This will be our first live website.

We need a website designed and business card design for our start-up in Switzerland. We also need the Web design to be converted into HTML and CSS files.

Function of website:
• To inform potential customers of our services
• Form a key part of our digital marketing and sales footprint.
• Branding

Please find attached logo.
Updates

Project Deadline Extended Reason: Giving us time to review submissions and provide opportunity for more submissions. Added Thursday, February 16, 2017

Reason: Looking for more idea's not necessarily set on blue and grey colours only.

Target Market(s)

B2B tech powered legal services.

Industry/Entity Type

Legal

Contact Information for Business Card

Lean and slick design.

Coding

Coded - Design and coding required

Number of Pages Required

5+ page

Requirements
Must have
• VERY LEAN AND CLEAN DESIGN!
• We have received many great standard designs, but we are looking for something more out-of-the box: You can get inspiration from these designs: http://www.pindelsite.com/websites/clean/
• Thanks!!
• Easy content management system
• Well structured coding for additional development
• Responsive webpage for all types of devices
• SEO optimized
• Tabs (Home, services, team, careers, blog, contact us)
• Colour scheme complementary to logo
Nice to have
• Look and Design - Approachable, High-tech, Modern
• Easy to add chat bot capability in future
Should not have
• Too busy/ too much clutter
• Not take to long to load

```html
<!DOCTYPE html>
<html lang="en">
<head>
<meta charset="utf-8">
<title>TAVO – Contact</title>
<link href="https://fonts.googleapis.com/css2?family=Josefin+Sans:wght@600;700&family=Lato:wght@400;700&display=swap" rel="stylesheet">
<style>
  :root {
    --accent: #e0332b;
    --text: #5a5a5a;
    --label: #8a8a8a;
    --field-border: #dcdcdc;
    --page: #ffffff;
    --band: #f4f4f4;
    --footer: #848484;
    --footer-text: #ffffff;
    --rule: #e2e2e2;
  }
  * { box-sizing: border-box; margin: 0; padding: 0; }
  html, body {
    width: 1200px; height: 811px; overflow: hidden;
    background: var(--page);
    font-family: "Lato", sans-serif;
    color: var(--text);
  }
  .page { position: relative; width: 1200px; height: 811px; border-top: 1px solid var(--rule); }

  .contact { position: relative; height: 452px; }
  .contact__title {
    position: absolute; top: 84px; left: 0; width: 1200px; text-align: center;
    font-family: "Josefin Sans", sans-serif; font-weight: 700;
    font-size: 19px; letter-spacing: 1.6px; color: var(--accent); text-transform: uppercase;
  }
  .contact__intro {
    position: absolute; top: 128px; left: 0; width: 1200px; text-align: center;
    font-size: 15px; letter-spacing: 0.6px; color: var(--text);
  }
  .field {
    position: absolute; left: 112px; width: 462px; height: 44px;
    border: 1px solid var(--field-border); border-radius: 3px; background: var(--page);
    padding: 0 13px; display: flex; align-items: center;
  }
  .field--name { top: 198px; }
  .field--phone { top: 256px; }
  .field--email { top: 315px; }
  .field--message {
    left: 624px; top: 198px; width: 460px; height: 109px; align-items: flex-start; padding-top: 10px;
  }
  .field__label {
    font-family: "Josefin Sans", sans-serif; font-weight: 700;
    font-size: 12px; letter-spacing: 1.3px; color: var(--label); text-transform: uppercase;
  }
  .send-button {
    position: absolute; left: 916px; top: 314px; width: 168px; height: 45px;
    background: var(--accent); border-radius: 3px; border: none;
    color: #fff; font-family: "Josefin Sans", sans-serif; font-weight: 700;
    font-size: 14px; letter-spacing: 1.8px; text-transform: uppercase;
    display: flex; align-items: center; justify-content: center; padding-top: 2px;
  }

  .details { position: absolute; top: 453px; left: 0; width: 1200px; height: 222px; background: var(--band); }
  .detail { position: absolute; top: 60px; width: 400px; text-align: center; }
  .detail--phone { left: -1px; }
  .detail--place { left: 400px; }
  .detail--mail { left: 785px; }
  .detail__icon { height: 22px; display: flex; justify-content: center; align-items: center; }
  .detail__text { margin-top: 41px; font-size: 15.5px; font-weight: 700; letter-spacing: 0.6px; color: var(--text); }

  .site-footer { position: absolute; top: 675px; left: 0; width: 1200px; height: 136px; background: var(--footer); color: var(--footer-text); text-align: center; }
  .site-footer__title {
    position: absolute; top: 23px; width: 100%;
    font-family: "Josefin Sans", sans-serif; font-weight: 700; font-size: 14px; letter-spacing: 1.3px; text-transform: uppercase;
  }
  .footer-nav { position: absolute; top: 65px; width: 100%; display: flex; justify-content: center; gap: 31px; }
  .footer-nav__link {
    font-family: "Josefin Sans", sans-serif; font-weight: 700; font-size: 14px; letter-spacing: 1.5px; text-transform: uppercase; color: var(--footer-text);
  }
  .social { position: absolute; top: 102px; width: 100%; display: flex; justify-content: center; gap: 13px; }
  .social__dot { width: 12px; height: 12px; border-radius: 50%; background: var(--footer-text); }
</style>
</head>
<body>
<div class="page">
  <section class="contact">
    <h2 class="contact__title">Let's get in touch!</h2>
    <p class="contact__intro">Ready to start your next project with us? That's great! Give us a call or send us an email and we will get back to you as soon as possible!</p>
    <div class="field field--name"><span class="field__label">Name</span></div>
    <div class="field field--phone"><span class="field__label">Phone</span></div>
    <div class="field field--email"><span class="field__label">Email</span></div>
    <div class="field field--message"><span class="field__label">Message</span></div>
    <div class="send-button">Send</div>
  </section>

  <section class="details">
    <div class="detail detail--phone">
      <div class="detail__icon">
        <svg width="10" height="17" viewBox="0 0 10 17"><rect x="0.5" y="0.5" width="9" height="16" rx="1.5" fill="#666"/><rect x="2" y="2.5" width="6" height="10" fill="#f4f4f4"/><circle cx="5" cy="14.5" r="0.9" fill="#f4f4f4"/></svg>
      </div>
      <p class="detail__text">041.555.0186</p>
    </div>
    <div class="detail detail--place">
      <div class="detail__icon">
        <svg width="14" height="20" viewBox="0 0 14 20"><path d="M7 0C3.1 0 0 3.1 0 7c0 5 7 13 7 13s7-8 7-13c0-3.9-3.1-7-7-7z" fill="#666"/><circle cx="7" cy="7" r="2.6" fill="#f4f4f4"/></svg>
      </div>
      <p class="detail__text">Lindenweg 12, 8004 Zürich</p>
    </div>
    <div class="detail detail--mail">
      <div class="detail__icon">
        <svg width="23" height="18" viewBox="0 0 23 18"><rect x="1" y="1" width="21" height="16" rx="2" fill="none" stroke="#666" stroke-width="2"/><path d="M1.5 3l10 7 10-7" fill="none" stroke="#666" stroke-width="2"/></svg>
      </div>
      <p class="detail__text">hello@tavo-legal.ch</p>
    </div>
  </section>

  <footer class="site-footer">
    <h3 class="site-footer__title">More about us</h3>
    <nav class="footer-nav">
      <span class="footer-nav__link">Home</span>
      <span class="footer-nav__link">Cookie policy</span>
      <span class="footer-nav__link">Refunds</span>
      <span class="footer-nav__link">Terms and conditions</span>
      <span class="footer-nav__link">Privacy policy</span>
      <span class="footer-nav__link">Help/FAQ</span>
    </nav>
    <div class="social">
      <span class="social__dot"></span>
      <span class="social__dot"></span>
      <span class="social__dot"></span>
      <span class="social__dot"></span>
    </div>
  </footer>
</div>
</body>
</html>
```